Tidewell Outdoor Signage

We need an outdoor signage design for my company with new logo designed from makerhive. We do electrical, Air conditioning & Plumbing, installation, service, repairs and maintenance. The design shall be an eye catching that cannot miss ready it.

Industry/Entity Type

Electrical, Air conditioning, Plumbing

```html
<!DOCTYPE html>
<html lang="en">
<head>
<meta charset="utf-8">
<title>Tidewell Outdoor Signage</title>
<link rel="stylesheet" href="https://fonts.googleapis.com/css2?family=Poppins:wght@600;700&family=Open+Sans:wght@700&display=swap">
<style>
  :root {
    --orange: #f08c42;
    --red: #e52329;
    --blue: #1769ad;
    --band: #1d69ad;
    --white: #ffffff;
    --rule: #222222;
  }
  * { margin: 0; padding: 0; box-sizing: border-box; }
  html, body { width: 1200px; height: 655px; overflow: hidden; background: var(--white); }
  .sign { position: relative; width: 1200px; height: 655px; background: var(--white); }

  .brand-mark {
    position: absolute; left: 300px; top: 62px;
    width: 240px; height: 240px; border-radius: 50%;
    background: var(--orange);
  }
  .brand-name {
    position: absolute; left: 138px; top: 318px;
    font-family: "Poppins", sans-serif; font-weight: 700;
    font-size: 132px; line-height: 1; letter-spacing: -3px;
    color: var(--orange);
  }
  .trades {
    position: absolute; left: 138px; top: 452px;
    display: flex; gap: 18px;
    font-family: "Open Sans", sans-serif; font-weight: 700; font-size: 27px; line-height: 1.2;
  }
  .trade--electrical { color: var(--red); }
  .trade--air { color: var(--blue); }
  .trade--plumbing { color: var(--orange); }

  .contact { position: absolute; left: 790px; top: 256px; width: 350px; }
  .divider { position: relative; height: 40px; }
  .divider::before {
    content: ""; position: absolute; left: 0; right: 0; top: 20px;
    border-top: 1.5px solid var(--rule);
  }
  .divider-icon {
    position: absolute; left: 167px; top: 1px; width: 38px; height: 38px;
    border-radius: 50%; background: var(--red);
    display: flex; align-items: center; justify-content: center;
  }
  .phone {
    font-family: "Poppins", sans-serif; font-weight: 700; font-size: 58px;
    color: var(--blue); line-height: 1; margin: 10px 0 28px; white-space: nowrap; letter-spacing: -1px;
  }
  .web {
    font-family: "Poppins", sans-serif; font-weight: 600; font-size: 20px;
    color: var(--blue); line-height: 1.65; margin-top: 6px; white-space: nowrap;
  }

  .services {
    position: absolute; left: 0; top: 540px; width: 1200px; height: 74px;
    background: var(--band);
    display: flex; align-items: center; justify-content: center; gap: 22px;
  }
  .service {
    display: flex; align-items: center; gap: 10px;
    font-family: "Poppins", sans-serif; font-weight: 700; font-size: 33px;
    color: var(--white); letter-spacing: 0.3px; line-height: 1;
  }
  .service-tick { width: 40px; height: 32px; flex: none; }
</style>
</head>
<body>
  <main class="sign">
    <div class="brand-mark"></div>
    <h1 class="brand-name">Tidewell</h1>
    <p class="trades">
      <span class="trade--electrical">Electrical</span>
      <span class="trade--air">Air Conditioning</span>
      <span class="trade--plumbing">Plumbing</span>
    </p>

    <section class="contact">
      <div class="divider">
        <span class="divider-icon">
          <svg width="20" height="20" viewBox="0 0 24 24" fill="none" stroke="#fff" stroke-width="2" stroke-linecap="round" stroke-linejoin="round">
            <path d="M22 16.9v3a2 2 0 0 1-2.2 2 19.8 19.8 0 0 1-8.6-3.1 19.5 19.5 0 0 1-6-6A19.8 19.8 0 0 1 2.1 4.2 2 2 0 0 1 4.1 2h3a2 2 0 0 1 2 1.7c.1.9.4 1.8.7 2.7a2 2 0 0 1-.5 2.1L8 9.8a16 16 0 0 0 6 6l1.3-1.3a2 2 0 0 1 2.1-.4c.9.3 1.8.6 2.7.7a2 2 0 0 1 1.7 2z"/>
          </svg>
        </span>
      </div>
      <p class="phone">0400 512 873</p>
      <div class="divider">
        <span class="divider-icon">
          <svg width="22" height="22" viewBox="0 0 24 24" fill="none" stroke="#fff" stroke-width="2">
            <circle cx="12" cy="12" r="9"/>
            <ellipse cx="12" cy="12" rx="4" ry="9"/>
            <line x1="3" y1="12" x2="21" y2="12"/>
          </svg>
        </span>
      </div>
      <p class="web">info@tidewellelectrical.com.au<br>www.tidewellelectrical.com.au</p>
    </section>

    <section class="services">
      <span class="service">
        <svg class="service-tick" viewBox="0 0 40 32"><path d="M2 17 L8 14 L15 24 Q24 10 39 1 Q26 14 15 31 Z" fill="var(--orange)"/></svg>
        INSTALLATION
      </span>
      <span class="service">
        <svg class="service-tick" viewBox="0 0 40 32"><path d="M2 17 L8 14 L15 24 Q24 10 39 1 Q26 14 15 31 Z" fill="var(--orange)"/></svg>
        SERVICE
      </span>
      <span class="service">
        <svg class="service-tick" viewBox="0 0 40 32"><path d="M2 17 L8 14 L15 24 Q24 10 39 1 Q26 14 15 31 Z" fill="var(--orange)"/></svg>
        REPAIRS AND MAINTENANCE
      </span>
    </section>
  </main>
</body>
</html>
```